Business Card design for shipping company 'FERNHOLT INTERNATIONAL LTD'

Classic / traditional business card in black Garamond / Times New Roman or similar text for a shipping / marine transport company, containing the following information:

QUOTE

FERNHOLT INTERNATIONAL LTD

MARTIN QUESTEDGE FICS

T: +44 7902 615370
E: cargo@fernholt-example.com

UNQUOTE

Target Market(s)

Marine / Shipping industry

Contact Information for Business Card

FERNHOLT INTERNATIONAL LTD MARTIN QUESTEDGE FICS T: +44 7902 615370 E: cargo@fernholt-example.com

Font styles to use
Serif

Colors

Designer to choose colors to be used in the design.

Requirements
Must have
• Garamond / Times New Roman or similar text in black colour

```html
<!DOCTYPE html>
<html lang="en">
<head>
<meta charset="utf-8">
<title>Fernholt International Ltd – Business Card</title>
<link rel="stylesheet" href="https://fonts.googleapis.com/css2?family=Tinos:wght@400;700&family=Poppins:wght@400;500&display=swap">
<style>
  :root {
    --stage: #b3b3b3;
    --navy-deep: #0a1538;
    --navy: #13255e;
    --navy-glow: #2a4590;
    --accent: #8ea3f4;
    --paper: #ffffff;
    --ink: #1e1e1e;
    --sketch: #dfe4ef;
  }
  * { margin: 0; padding: 0; box-sizing: border-box; }
  html, body { width: 1200px; height: 868px; overflow: hidden; }
  body { background: var(--stage); position: relative; }

  .card {
    position: absolute;
    top: 133px;
    width: 344px;
    height: 600px;
    overflow: hidden;
    background:
      radial-gradient(ellipse 60% 45% at 58% 38%, var(--navy-glow) 0%, rgba(42,69,144,0) 70%),
      linear-gradient(180deg, var(--navy-deep) 0%, var(--navy) 55%, var(--navy-deep) 100%);
    box-shadow: 6px 8px 10px rgba(0,0,0,0.35);
  }
  .card--front { left: 242px; }
  .card--back  { left: 647px; }

  .wordmark {
    position: absolute;
    font-family: "Tinos", "Times New Roman", serif;
    font-weight: 400;
    color: var(--paper);
    text-align: center;
  }
  .wordmark__name { display: block; letter-spacing: 2px; line-height: 1; }
  .wordmark__sub  { display: block; letter-spacing: 3px; line-height: 1; }

  .card--front .wordmark { left: 45px; top: 50px; width: 155px; }
  .card--front .wordmark__name { font-size: 19px; }
  .card--front .wordmark__sub  { font-size: 7.5px; margin-top: 4px; }

  .card--back .wordmark { left: 0; top: 262px; width: 344px; }
  .card--back .wordmark__name { font-size: 26px; letter-spacing: 2.5px; }
  .card--back .wordmark__sub  { font-size: 11px; margin-top: 6px; letter-spacing: 3.5px; }

  .person {
    position: absolute;
    left: 45px;
    top: 138px;
    font-family: "Tinos", "Times New Roman", serif;
    font-weight: 700;
    font-size: 32px;
    line-height: 29px;
    letter-spacing: 1px;
    color: var(--paper);
  }
  .person__first { display: block; color: var(--accent); }
  .person__last, .person__post { display: block; }

  .role {
    position: absolute;
    left: 46px;
    top: 241px;
    font-family: "Poppins", sans-serif;
    font-size: 15px;
    letter-spacing: 2.5px;
    color: var(--accent);
  }

  .ship-art {
    position: absolute;
    background: linear-gradient(180deg, rgba(223,228,239,0) 0%, rgba(223,228,239,0.55) 60%, var(--sketch) 100%);
  }
  .card--front .ship-art { left: 0; top: 338px; width: 290px; height: 104px; }
  .card--back  .ship-art { left: 175px; top: 515px; width: 169px; height: 80px; }

  .contact-panel {
    position: absolute;
    left: 0;
    top: 440px;
    width: 344px;
    height: 160px;
    background: var(--paper);
  }
  .card--back .base-strip {
    position: absolute;
    left: 0; top: 595px;
    width: 344px; height: 5px;
    background: var(--paper);
  }

  .contact-list { list-style: none; position: absolute; left: 37px; top: 53px; }
  .contact-list__item {
    display: flex;
    align-items: center;
    height: 24px;
    margin-bottom: 9px;
    font-family: "Poppins", sans-serif;
    font-size: 15px;
    color: var(--ink);
  }
  .contact-list__icon {
    width: 22px; height: 22px;
    border-radius: 50%;
    background: var(--accent);
    margin-right: 10px;
    display: flex; align-items: center; justify-content: center;
  }
  .contact-list__icon svg { width: 12px; height: 12px; }
</style>
</head>
<body>

  <section class="card card--front">
    <div class="wordmark">
      <span class="wordmark__name">FERNHOLT</span>
      <span class="wordmark__sub">INTERNATIONAL LTD</span>
    </div>

    <h1 class="person">
      <span class="person__first">MARTIN</span>
      <span class="person__last">QUESTEDGE</span>
      <span class="person__post">FICS</span>
    </h1>
    <p class="role">OWNER</p>

    <div class="ship-art" role="img" aria-label="White line sketch of a cargo ship sailing on the sea"></div>

    <div class="contact-panel">
      <ul class="contact-list">
        <li class="contact-list__item">
          <span class="contact-list__icon">
            <svg viewBox="0 0 24 24" fill="#0a1538"><path d="M6.6 10.8a15.1 15.1 0 0 0 6.6 6.6l2.2-2.2a1 1 0 0 1 1-.25 11.4 11.4 0 0 0 3.6.57 1 1 0 0 1 1 1V20a1 1 0 0 1-1 1A17 17 0 0 1 3 4a1 1 0 0 1 1-1h3.5a1 1 0 0 1 1 1c0 1.25.2 2.45.57 3.57a1 1 0 0 1-.25 1z"/></svg>
          </span>
          +44 7902 615370
        </li>
        <li class="contact-list__item">
          <span class="contact-list__icon">
            <svg viewBox="0 0 24 24" fill="#0a1538"><path d="M2 5h20v14H2z" opacity="1"/><path d="M2 5l10 8 10-8" fill="none" stroke="#8ea3f4" stroke-width="1.8"/></svg>
          </span>
          cargo@fernholt-example.com
        </li>
      </ul>
    </div>
  </section>

  <section class="card card--back">
    <div class="wordmark">
      <span class="wordmark__name">FERNHOLT</span>
      <span class="wordmark__sub">INTERNATIONAL LTD</span>
    </div>
    <div class="ship-art" role="img" aria-label="White line sketch of a cargo ship bow entering from the right"></div>
    <div class="base-strip"></div>
  </section>

</body>
</html>
```